Bubble-Diagramm als Infografik für unseren Kunden aus der Immobilienbranche
Zielgruppe
Wir sind ein Software-Unternehmen mit Kunden aus allen Branchen. Ganz generell für unsere Homepage, konkret aber auch im Rahmen eines Kundenprojektes suchen wir ansprechende Beispiele und kreative Visualisierungen, wie Diagramme zu bestimmten Sachverhalten dargestellt werden können.
Aufgabenstellung
Wir möchten die Möglichkeiten darstellen, mit excelbasierten Diagrammtypen den gewissen „Wow-Effekt“ bei unseren Kunden hervorzurufen. Konkret geht es uns hier um die Erstellung eines Bubble-Diagramms. In einem Objektvergleich von Gewerbeimmobilien sollen drei Dimensionen (hier: Größe des Objekte, Gesamtmiete über die Laufzeit, effektive Miete je Quadratmeter) im Bubble-Diagramm dargestellt werden. Siehe hierzu Entwurf (.xls-Datei) anbei.
Eine Orientierung an unserem Firmenlayout (www.brenolux-net.de) ist ausdrücklich erwünscht. Die Grafik sollte aufgeräumt und klar wirken, ohne nüchtern zu sein, um auf der einen Seite mit der Form nicht vom Inhalt abzulenken, und sich auf der anderen Seite aber eben doch über die Form von der Konkurrenz, die nur mit Excel-Bordmitteln arbeitet, erkennbar abzuheben. Denkbar sind grundsätzlich auch Piktogramme oder vergleichbare, Inhalt transportierende Elemente im Graphik-Hintergrund oder in der Umrahmung, immer unter der Maßgabe, dass sie nicht zu verspielt daherkommen.
Technisch sind wir in der Lage, Excel-Diagramme auch „interaktiv“ zu gestalten, also nach Klick auf ein Diagrammelement ein Kontextmenü oder erweiterte Informationen einzublenden. Daher wünschen wir uns als Teil des Entwurfs, beispielhaft für eine Blase, die Darstellung so eines interaktiven Elements: eines Kontextmenüs / und oder eines Datenblatts.
Vorzugsweise soll die Grafik im Excel-Format zur Verfügung gestellt werden, das ist aber kein Must-have.

```html
<!DOCTYPE html>
<html lang="de">
<head>
<meta charset="utf-8">
<title>Bubble-Diagramm Objektvergleich</title>
<link href="https://fonts.googleapis.com/css2?family=Barlow:wght@400;500;600;700&display=swap" rel="stylesheet">
<style>
  :root {
    --page-bg: #e4e4e4;
    --panel-bg: #f4f4f4;
    --cyan: #00f0f4;
    --teal: #1ab8bd;
    --teal-dark: #12a3a8;
    --grid-line: #d4f5f7;
    --tick-blue: #8cb8f2;
    --label-teal: #19b3b8;
    --white: #ffffff;
    --yellow: #f8c63e;
    --yellow-light: #fcd874;
    --orange: #f4b33a;
    --orange-text: #b97b10;
    --pink: #c53a8a;
    --green: #1c9f86;
    --purple: #4b2fa0;
  }
  html, body {
    margin: 0;
    padding: 0;
    width: 900px;
    height: 1200px;
    overflow: hidden;
    background: var(--page-bg);
    font-family: "Barlow", Arial, sans-serif;
  }
  .canvas {
    position: relative;
    width: 900px;
    height: 1200px;
  }
  .chart-panel {
    position: absolute;
    left: 20px;
    top: 358px;
    width: 860px;
    height: 484px;
    background: var(--panel-bg);
    box-shadow: 0 2px 10px rgba(0,0,0,0.08);
  }
  .chart-panel svg { display: block; width: 100%; height: 100%; }
  .tick-label { font-weight: 600; font-size: 20px; fill: var(--tick-blue); }
  .tick-label--on-fill { fill: var(--white); }
  .axis-value { font-weight: 600; font-size: 24px; fill: var(--white); }
  .axis-title { font-weight: 700; font-size: 28px; fill: var(--label-teal); }
  .legend-text { font-weight: 500; font-size: 19px; fill: var(--label-teal); }
  .callout-small { font-weight: 700; font-size: 13px; fill: var(--orange-text); }
  .callout-big { font-weight: 700; font-size: 24px; fill: var(--white); }
</style>
</head>
<body>
<div class="canvas">
  <section class="chart-panel">
    <svg viewBox="0 0 1420 800" aria-label="Bubble-Diagramm: Effektivmiete je m² über Gesamtmiete">
      <defs>
        <clipPath id="plot-area">
          <polygon points="275,70 1160,70 1160,665 275,585"/>
        </clipPath>
        <radialGradient id="fill-yellow" cx="40%" cy="35%" r="70%">
          <stop offset="0" stop-color="#ffe08a"/><stop offset="1" stop-color="#f2b52c"/>
        </radialGradient>
        <radialGradient id="fill-pink" cx="40%" cy="35%" r="70%">
          <stop offset="0" stop-color="#e0589e"/><stop offset="1" stop-color="#a82a75"/>
        </radialGradient>
        <radialGradient id="fill-green" cx="40%" cy="35%" r="70%">
          <stop offset="0" stop-color="#2fbf9f"/><stop offset="1" stop-color="#11806c"/>
        </radialGradient>
        <radialGradient id="fill-purple" cx="40%" cy="35%" r="70%">
          <stop offset="0" stop-color="#6a45c4"/><stop offset="1" stop-color="#3a1f85"/>
        </radialGradient>
      </defs>

      <!-- floor shadow -->
      <polygon points="230,600 1160,680 1120,720 240,615" fill="#e6e6e6"/>

      <!-- plot -->
      <g class="plot" clip-path="url(#plot-area)">
        <rect x="275" y="60" width="900" height="620" fill="var(--white)"/>
        <path class="rent-curve" fill="var(--cyan)"
              d="M275,455 C330,470 390,470 450,455 C540,430 620,410 720,360 C820,310 880,265 960,235 C1040,212 1100,210 1160,215 L1160,680 L275,680 Z"/>
        <g class="grid" stroke="var(--grid-line)" stroke-width="2.5">
          <line x1="275" y1="75" x2="1160" y2="70"/>
          <line x1="275" y1="126" x2="1160" y2="130"/>
          <line x1="275" y1="177" x2="1160" y2="189"/>
          <line x1="275" y1="228" x2="1160" y2="249"/>
          <line x1="275" y1="279" x2="1160" y2="308"/>
          <line x1="275" y1="330" x2="1160" y2="368"/>
          <line x1="275" y1="381" x2="1160" y2="427"/>
          <line x1="275" y1="432" x2="1160" y2="487"/>
          <line x1="275" y1="483" x2="1160" y2="546"/>
          <line x1="275" y1="534" x2="1160" y2="606"/>
          <line x1="350" y1="70" x2="350" y2="600"/>
          <line x1="430" y1="70" x2="430" y2="600"/>
          <line x1="510" y1="70" x2="510" y2="610"/>
          <line x1="595" y1="70" x2="593" y2="620"/>
          <line x1="680" y1="70" x2="678" y2="630"/>
          <line x1="770" y1="70" x2="767" y2="640"/>
          <line x1="862" y1="70" x2="859" y2="650"/>
          <line x1="958" y1="70" x2="955" y2="660"/>
          <line x1="1058" y1="70" x2="1055" y2="670"/>
        </g>
      </g>

      <!-- axes -->
      <rect x="258" y="68" width="17" height="527" fill="var(--teal)"/>
      <polygon points="258,585 1160,665 1160,675 1140,680 258,597" fill="var(--teal)"/>

      <!-- tick labels -->
      <text class="tick-label" x="282" y="97">25 €</text>
      <text class="tick-label" x="282" y="350">20 €</text>
      <text class="tick-label tick-label--on-fill" x="282" y="549">15 €</text>
      <text class="tick-label tick-label--on-fill" x="282" y="575">5 Mio €</text>
      <text class="axis-value" x="682" y="614">10 Mio €</text>
      <text class="axis-value" x="1058" y="648">15 Mio €</text>

      <!-- axis titles -->
      <text class="axis-title" transform="translate(231,205) rotate(-90)" text-anchor="middle">Effektivmiete je m²</text>
      <text class="axis-title" x="280" y="648">Gesamtmiete</text>
      <line x1="275" y1="666" x2="885" y2="666" stroke="var(--cyan)" stroke-width="2"/>

      <!-- bubbles -->
      <g class="bubble bubble--house">
        <circle cx="502" cy="450" r="56" fill="var(--teal)"/>
        <circle cx="495" cy="445" r="48" fill="url(#fill-yellow)" stroke="#fbe29a" stroke-width="3"/>
        <path d="M470,447 L495,423 L520,447 Z M475,447 h40 v22 h-40 Z" fill="none" stroke="var(--white)" stroke-width="5" stroke-linejoin="round"/>
        <path d="M485,452 h20 v14 h-20 Z M495,452 v14 M485,459 h20" fill="none" stroke="var(--white)" stroke-width="3"/>
      </g>
      <g class="bubble bubble--tower">
        <circle cx="588" cy="405" r="47" fill="var(--teal)"/>
        <circle cx="582" cy="400" r="40" fill="url(#fill-pink)"/>
        <rect x="566" y="380" width="32" height="40" fill="var(--white)"/>
        <g fill="var(--pink)">
          <rect x="570" y="385" width="4" height="5"/><rect x="578" y="385" width="4" height="5"/><rect x="586" y="385" width="4" height="5"/>
          <rect x="570" y="394" width="4" height="5"/><rect x="578" y="394" width="4" height="5"/><rect x="586" y="394" width="4" height="5"/>
          <rect x="570" y="403" width="4" height="5"/><rect x="578" y="403" width="4" height="5"/><rect x="586" y="403" width="4" height="5"/>
          <rect x="578" y="412" width="8" height="8"/>
        </g>
      </g>
      <g class="bubble bubble--office">
        <circle cx="675" cy="378" r="63" fill="var(--teal)"/>
        <circle cx="668" cy="372" r="55" fill="url(#fill-green)"/>
        <rect x="644" y="356" width="20" height="38" fill="var(--white)"/>
        <rect x="666" y="344" width="28" height="50" fill="var(--white)"/>
        <g fill="var(--green)">
          <rect x="648" y="362" width="5" height="5"/><rect x="656" y="362" width="5" height="5"/>
          <rect x="648" y="372" width="5" height="5"/><rect x="656" y="372" width="5" height="5"/>
          <rect x="648" y="382" width="5" height="5"/><rect x="656" y="382" width="5" height="5"/>
          <rect x="670" y="350" width="20" height="3"/><rect x="670" y="357" width="20" height="3"/>
          <rect x="670" y="364" width="20" height="3"/><rect x="670" y="371" width="20" height="3"/>
          <rect x="670" y="378" width="20" height="3"/>
        </g>
      </g>
      <g class="bubble bubble--complex">
        <circle cx="865" cy="318" r="80" fill="var(--teal)"/>
        <circle cx="857" cy="310" r="72" fill="url(#fill-purple)"/>
        <rect x="812" y="285" width="22" height="55" fill="var(--white)"/>
        <rect x="838" y="268" width="30" height="72" fill="var(--white)"/>
        <rect x="872" y="290" width="22" height="50" fill="var(--white)"/>
        <g fill="var(--purple)">
          <rect x="817" y="292" width="5" height="6"/><rect x="825" y="292" width="5" height="6"/>
          <rect x="817" y="304" width="5" height="6"/><rect x="825" y="304" width="5" height="6"/>
          <rect x="817" y="316" width="5" height="6"/><rect x="825" y="316" width="5" height="6"/>
          <rect x="843" y="276" width="5" height="8"/><rect x="851" y="276" width="5" height="8"/><rect x="859" y="276" width="5" height="8"/>
          <rect x="843" y="290" width="5" height="8"/><rect x="851" y="290" width="5" height="8"/><rect x="859" y="290" width="5" height="8"/>
          <rect x="843" y="304" width="5" height="8"/><rect x="851" y="304" width="5" height="8"/><rect x="859" y="304" width="5" height="8"/>
          <rect x="849" y="326" width="9" height="14"/>
          <rect x="876" y="297" width="14" height="3"/><rect x="876" y="305" width="14" height="3"/>
          <rect x="876" y="313" width="14" height="3"/><rect x="876" y="321" width="14" height="3"/>
        </g>
      </g>

      <!-- data sheet callout -->
      <g class="callout">
        <path d="M403,193 H541 A45,45 0 0 1 586,238 V300 A45,45 0 0 1 541,345 H470 V390 L430,345 H403 A45,45 0 0 1 358,300 V238 A45,45 0 0 1 403,193 Z" fill="var(--yellow-light)"/>
        <path d="M403,193 H470 V345 H430 L430,345 H403 A45,45 0 0 1 358,300 V238 A45,45 0 0 1 403,193 Z" fill="var(--orange)"/>
        <rect x="389" y="215" width="60" height="60" rx="6" fill="none" stroke="var(--orange-text)" stroke-width="4"/>
        <path d="M400,264 L438,226 M424,226 H438 V240 M400,250 V264 H414" fill="none" stroke="var(--orange-text)" stroke-width="4"/>
        <text class="callout-small" x="419" y="295" text-anchor="middle">Größe</text>
        <text class="callout-big" x="419" y="318" text-anchor="middle">8.500M²</text>
        <text class="callout-small" x="478" y="230">Gesamtmiete</text>
        <text class="callout-big" x="477" y="254">10 Mio €</text>
        <text class="callout-small" x="478" y="295">Effektivmiete</text>
        <text class="callout-big" x="477" y="318">20.30 €</text>
      </g>

      <!-- legend -->
      <circle cx="96" cy="735" r="19" fill="url(#fill-yellow)" stroke="var(--cyan)" stroke-width="3"/>
      <text class="legend-text" x="134" y="747">Die Größe der Blasen zeigt die Objektgröße an.</text>
    </svg>
  </section>
</div>
</body>
</html>
```